TrelWave Agile Coaching Website

I need an updated website for www.trelwave-demo.com. I'm looking for a modern look. This is a professional site, but I don't want it to look "stuffy". It needs to have an element of fun and learning.

My services include:
Lean Agile Coaching
Lean Agile Training
Facilitation
Workshops
Consulting

Ideas this site should convey: collaboration, learning, teamwork, adaptability, flow, limited WIP, agility, Lean.

I would like to use some of my own photos and slide decks for content: http://www.deckshelf-example.net/mirabrecken/presentations

I would also like to include the WorkWeb recommendations I have from customers: https://www.workweb-example.com/in/mirabrecken

Examples of sites I like:
http://www.corvalpine-example.com
http://www.stridemoss-example.com

Target Market(s)

IT professionals, software development managers

Industry/Entity Type

It Company

Coding

Coded - Design and coding required

Font styles to use
Serif
Sans Serif

Requirements
Must have
• Original looking graphics and layout.
• My logo must be included in layout.
• Need to feature my blog content.
• Deliverable must be a WordPress theme that I can install.
• Responsive site.
Nice to have
• Use images from my slides on DeckShelf if they make sense.

```html
<!DOCTYPE html>
<html lang="en">
<head>
<meta charset="utf-8">
<title>TrelWave — Lean Agile Coaching</title>
<link href="https://fonts.googleapis.com/css2?family=Roboto:wght@400;500;700&family=Roboto+Condensed:wght@400;700&family=Nothing+You+Could+Do&display=swap" rel="stylesheet">
<style>
  :root {
    --ink: #1c1c1c;
    --muted: #5a5a5a;
    --green: #3cc52c;
    --band: #d9d9d9;
    --panel: #dcdcdc;
    --white: #ffffff;
    --hero-a: #6f7a8c;
    --hero-b: #a9b4c4;
    --hero-c: #4f6686;
    --dash: #c4c4c4;
    --icon: #bdbdbd;
    --logo-dot: #9a9a9a;
  }
  * { box-sizing: border-box; margin: 0; padding: 0; }
  html, body { width: 1200px; height: 676px; overflow: hidden; background: var(--white); }
  body { font-family: "Roboto", sans-serif; color: var(--ink); position: relative; }
  a { text-decoration: none; color: inherit; }

  .topbar {
    position: absolute; top: 0; left: 0; width: 1200px; height: 38px;
    display: flex; align-items: center; justify-content: flex-end; gap: 26px;
    padding-right: 40px; font-family: "Roboto Condensed", sans-serif; font-size: 14px; color: var(--muted);
  }
  .topbar__item { display: flex; align-items: center; gap: 5px; }
  .topbar__login {
    background: var(--green); color: var(--white); font-weight: 700; font-size: 12px;
    padding: 2px 7px; border-radius: 3px;
  }
  .topbar__social { display: flex; gap: 14px; }
  .topbar__social span { width: 14px; height: 14px; border-radius: 50%; background: #9a9a9a; display: block; }

  .navband {
    position: absolute; top: 38px; left: 0; width: 1200px; height: 72px; background: var(--band);
  }
  .nav {
    position: absolute; right: 40px; top: 26px; display: flex; gap: 36px;
    font-family: "Roboto Condensed", sans-serif; font-size: 16px; color: #333; letter-spacing: .3px;
  }
  .nav a.is-active { color: var(--ink); font-weight: 700; }

  .logo {
    position: absolute; top: 26px; left: 40px; width: 290px; height: 100px; z-index: 3;
    background: var(--white); border-radius: 0 0 6px 6px;
    display: flex; align-items: center; gap: 14px; padding-left: 24px;
  }
  .logo__dot { width: 22px; height: 22px; border-radius: 50%; background: var(--logo-dot); flex: none; }
  .logo__name { font-size: 44px; font-weight: 500; color: var(--ink); line-height: 1; }

  .hero {
    position: absolute; top: 110px; left: 0; width: 1200px; height: 370px;
    background: linear-gradient(115deg, var(--hero-a) 0%, var(--hero-b) 45%, #c9d2de 60%, var(--hero-c) 100%);
  }
  .hero__content {
    position: absolute; top: 115px; left: 0; width: 1200px; text-align: center; color: var(--white);
  }
  .hero__title { font-family: "Nothing You Could Do", cursive; font-size: 60px; font-weight: 400; line-height: 1; }
  .hero__text { margin-top: 26px; font-size: 16px; line-height: 20px; }
  .hero__actions { margin-top: 30px; display: flex; justify-content: center; gap: 34px; }
  .btn {
    background: var(--white); color: var(--ink); font-family: "Roboto Condensed", sans-serif;
    font-size: 11px; font-weight: 700; padding: 9px 14px; border-radius: 2px;
  }

  .welcome {
    position: absolute; top: 445px; left: 85px; width: 1030px; height: 115px;
    background: var(--panel); border-radius: 3px; text-align: center; padding-top: 22px;
  }
  .welcome__title { font-size: 18px; font-weight: 500; }
  .welcome__text { margin-top: 16px; font-size: 13px; line-height: 18px; color: var(--muted); padding: 0 20px; }

  .services { position: absolute; top: 586px; left: 0; width: 1200px; text-align: center; }
  .services__title { font-size: 22px; font-weight: 500; }
  .services__title em { font-style: normal; color: var(--green); }
  .services__rule { margin: 14px auto 0; width: 1040px; border-top: 1px dashed var(--dash); }
  .services__icons { display: flex; justify-content: space-between; width: 880px; margin: 16px auto 0; }
  .services__icons span { width: 44px; height: 44px; border-radius: 50%; background: var(--icon); display: block; }
</style>
</head>
<body>
  <header class="topbar">
    <span class="topbar__item">
      <svg width="12" height="12" viewBox="0 0 24 24"><path fill="#7a7a7a" d="M6.6 10.8a15.1 15.1 0 0 0 6.6 6.6l2.2-2.2c.3-.3.7-.4 1-.2 1.1.4 2.3.6 3.6.6.6 0 1 .4 1 1V20c0 .6-.4 1-1 1C10.6 21 3 13.4 3 4c0-.6.4-1 1-1h3.5c.6 0 1 .4 1 1 0 1.3.2 2.5.6 3.6.1.3 0 .7-.2 1z"/></svg>
      +1 800 555 01 47
    </span>
    <span class="topbar__item">
      <svg width="13" height="10" viewBox="0 0 26 20"><rect x="1" y="1" width="24" height="18" fill="#7a7a7a"/><path d="M1 1l12 10L25 1" fill="none" stroke="#fff" stroke-width="2"/></svg>
      info@trelwave-demo.com
    </span>
    <span class="topbar__login">LOGIN</span>
    <span class="topbar__social"><span></span><span></span></span>
  </header>

  <div class="navband">
    <nav class="nav">
      <a class="is-active" href="#">HOME</a>
      <a href="#">ABOUT</a>
      <a href="#">SERVICES</a>
      <a href="#">BLOG</a>
      <a href="#">PRICING</a>
      <a href="#">CONTACT</a>
    </nav>
  </div>

  <a class="logo" href="#">
    <span class="logo__dot"></span>
    <span class="logo__name">TrelWave</span>
  </a>

  <section class="hero" role="img" aria-label="Blurred photo of a team meeting around a table with a laptop showing a bar chart">
    <div class="hero__content">
      <h1 class="hero__title">Understanding</h1>
      <p class="hero__text">
        Regardless if you are new to Agile and Lean, or your organization is now doing Agile,<br>
        a better understanding of the principles and practices is crucial for team and organizational improvement.<br>
        Education on the Lean-Agile principles helps software professionals focus on...
      </p>
      <div class="hero__actions">
        <a class="btn" href="#">READ MORE</a>
        <a class="btn" href="#">GO ON SURFING</a>
      </div>
    </div>
  </section>

  <section class="welcome">
    <h2 class="welcome__title">Welcome We're TrelWave</h2>
    <p class="welcome__text">TrelWave is a company dedicated to improving the art and science of software development for both the consumers of software services and the professionals doing the work. Our primary focus is the marketplace and community where we live—the Kansas City metro area.</p>
  </section>

  <section class="services">
    <h2 class="services__title">Our <em>Services</em></h2>
    <div class="services__rule"></div>
    <div class="services__icons"><span></span><span></span><span></span><span></span><span></span></div>
  </section>
</body>
</html>
```